Tobin's Jewelry Studio Needs a Moving Location Flyer

We need a flyer to inform our customers of our location moving. We will be moving to our city's downtown which is only 1 mile away from our current address. We will be having a moving sale ( Up to 80% off). The sale starts Sept. 8th Our business creates, sells, and repairs fine jewelry. Dimensions are 5"x8"

Target Market(s)

Women ages 25-55

Industry/Entity Type

Jewelry

Colors
85abd2
cfdeed

Requirements
Must have
• Our logo
• Mention of the sale
• Our current address
• 4785 Cresthaven Blvd.
• Dunmore, Ca 94318
• (415)826-3319
Nice to have
• Mention that we're relocating to downtown Dunmore (new location opening Nov. 1st.)

```html
<!DOCTYPE html>
<html lang="en">
<head>
<meta charset="utf-8">
<title>Tobin's Jewelry Studio – Relocation Flyer</title>
<link rel="stylesheet" href="https://fonts.googleapis.com/css2?family=Montserrat:wght@300;400;500;600;700&family=Oswald:wght@400;500&display=swap">
<style>
  :root {
    --page-bg: #9a9a9a;
    --paper: #ffffff;
    --sky: #85abd2;
    --mist: #cfdeed;
    --aqua: #bfe9ee;
    --ink: #1e1e1e;
    --slate: #5a5a5a;
    --band-grey: #7a7a7a;
    --rule-brown: #4a2a22;
    --sparkle-light: #f4f5f7;
    --sparkle-mid: #dfe1e5;
  }
  * { margin: 0; padding: 0; box-sizing: border-box; }
  html, body {
    width: 1200px; height: 1200px; overflow: hidden;
    background: var(--page-bg);
    font-family: "Montserrat", sans-serif;
  }
  .flyer {
    position: absolute; left: 40px; top: 250px;
    width: 1120px; height: 700px;
    background: var(--paper);
    overflow: hidden;
  }
  .sparkle-field {
    position: absolute; left: 440px; top: 330px; width: 680px; height: 270px;
    background: radial-gradient(ellipse at 40% 60%, var(--sparkle-light), var(--sparkle-mid));
  }
  .model-photo {
    position: absolute; left: 0; top: 0; width: 480px; height: 700px;
    background:
      radial-gradient(ellipse 60% 45% at 60% 40%, #f1d9cc 0%, rgba(241,217,204,0) 70%),
      linear-gradient(180deg, #ffffff 0%, #f3f3f5 55%, #e4e5e8 100%);
  }
  .rule-top {
    position: absolute; left: 480px; top: 112px; width: 640px; height: 3px;
    background: var(--rule-brown);
  }
  .brand {
    position: absolute; right: 30px; top: 58px;
    display: flex; align-items: center; gap: 12px;
  }
  .brand-dot {
    width: 44px; height: 44px; border-radius: 50%;
    background: var(--aqua);
  }
  .brand-name {
    font-weight: 600; font-size: 20px; color: var(--ink);
  }
  .headline {
    position: absolute; left: 480px; top: 135px; width: 620px;
    text-align: right; white-space: nowrap;
  }
  .headline-main {
    font-weight: 600; font-size: 58px; line-height: 1.05;
    color: var(--sky); letter-spacing: 2px;
  }
  .headline-sub {
    font-size: 40px; line-height: 1.2; color: var(--ink); letter-spacing: 1px;
  }
  .headline-sub .thin { font-weight: 300; }
  .headline-sub .city { font-weight: 700; }
  .opening-band {
    position: absolute; left: 480px; top: 266px; width: 640px; height: 64px;
    background: linear-gradient(90deg, var(--mist), var(--sky));
    display: flex; align-items: center; padding-left: 30px; gap: 18px;
    white-space: nowrap;
  }
  .opening-band .lead { font-weight: 300; font-size: 29px; color: var(--ink); }
  .opening-band .date { font-family: "Oswald", sans-serif; font-size: 30px; color: var(--ink); }
  .call {
    position: absolute; left: 500px; top: 350px; white-space: nowrap;
  }
  .call-label { font-weight: 500; font-size: 32px; color: var(--slate); letter-spacing: 1px; line-height: 1.2; }
  .call-phone {
    font-family: "Oswald", sans-serif; font-weight: 500;
    font-size: 44px; color: var(--sky); line-height: 1.1;
  }
  .address {
    position: absolute; left: 500px; top: 478px; color: var(--ink); white-space: nowrap;
  }
  .address-label { font-weight: 700; font-size: 21px; margin-bottom: 4px; }
  .address-line { font-size: 16px; }
  .rule-bottom {
    position: absolute; left: 440px; top: 600px; width: 680px; height: 3px;
    background: var(--rule-brown);
  }
  .footer-band {
    position: absolute; left: 440px; top: 610px; width: 680px; height: 90px;
    background: var(--band-grey);
    display: flex; align-items: center; padding-left: 50px;
  }
  .website {
    color: #ffffff; font-size: 20px; letter-spacing: 9px; white-space: nowrap;
  }
  .sale-badge {
    position: absolute; left: 880px; top: 350px; width: 220px; height: 220px;
  }
</style>
</head>
<body>
  <main class="flyer">
    <div class="sparkle-field"></div>
    <div class="model-photo" role="img" aria-label="Photo of a smiling woman wearing a pearl necklace, pearl bracelet and ring, resting her chin on her hand"></div>

    <div class="rule-top"></div>
    <div class="brand">
      <span class="brand-dot"></span>
      <span class="brand-name">Tobin's Jewelry Studio</span>
    </div>

    <div class="headline">
      <div class="headline-main">RELOCATING TO</div>
      <div class="headline-sub"><span class="thin">DOWNTOWN</span> <span class="city">DUNMORE</span></div>
    </div>

    <div class="opening-band">
      <span class="lead">New location opening</span>
      <span class="date">1st November</span>
    </div>

    <div class="call">
      <div class="call-label">CALL TODAY</div>
      <div class="call-phone">(415)826-3319</div>
    </div>

    <div class="address">
      <div class="address-label">New address</div>
      <div class="address-line">4785 Cresthaven Blvd, Dunmore, Ca 94318</div>
    </div>

    <div class="rule-bottom"></div>
    <div class="footer-band">
      <span class="website">www.tobinsjewelrystudio.com</span>
    </div>

    <svg class="sale-badge" viewBox="0 0 250 250" aria-label="Up to 80% off">
      <defs>
        <radialGradient id="badgeFill" cx="50%" cy="40%" r="60%">
          <stop offset="0" stop-color="#8e8e8e"/>
          <stop offset="1" stop-color="#5e5e5e"/>
        </radialGradient>
      </defs>
      <circle cx="125" cy="125" r="120" fill="#ffffff"/>
      <circle cx="125" cy="125" r="116" fill="none" stroke="#85abd2" stroke-width="6"/>
      <circle cx="125" cy="125" r="106" fill="url(#badgeFill)"/>
      <text x="125" y="82" text-anchor="middle" font-family="Montserrat, sans-serif" font-size="28" fill="#ffffff">UP TO</text>
      <text x="125" y="150" text-anchor="middle" font-family="Oswald, sans-serif" font-weight="500" font-size="72" fill="#bfe9ee">80%</text>
      <text x="125" y="200" text-anchor="middle" font-family="Montserrat, sans-serif" font-weight="300" font-size="44" fill="#ffffff">OFF</text>
    </svg>
  </main>
</body>
</html>
```